Stationary For Commercial Real Estate Company

We need a consistently branded image for our business cards, letterhead, property marketing flyers, powerpoint presentations, etc.

We are a COMMERCIAL real estate company. We do NOT do residential real estate, so please do not submit any designs with references to houses as they will be rejected.

We just completed a design contest for our logo, so we want to encorporate that logo in our stationary design, and we have attached it for your use. Please let us know if you need the logo in another format.

We can accept the business cards in adobe illustrator, the letterhead needs to be a template in Microsoft Word, the Property Flyer can be either in PowerPoint or Adobe Illustrator, and the PowerPoint presentation needs to have a Cover Page, Table of Contents, a few sample pages, and a Closing/Summary slide at the end.

We have attached a sample Property Flyer to show what we are basically looking for; but this is only provided as a sample, so you can see the kind of information we generally need to include on our Flyers. They can be in either landscape or portrait layout.

Target Market(s)

CEO and Upper Level managers who are decision makers regarding commercial real estate projects. Local, regional and fortune 500 clients.

Industry/Entity Type

Real Estate

Requirements
Must have
• There must be a space on the Flyer that includes the disclaimer shown on the bottom of the attached sample.
Nice to have
• I appreciate the designs submitted so far, but I'd prefer not to have watermarks on the letterhead or business cards. I'm not sure I'm a big fan of the watermarks.

Also, I'd like to see some color combinations that use something other than just red. I'd like to see something where we have just the logo in red and use other contrasting colors on the letterhead or business cards.
Should not have
• Please, no references to houses or anything else that suggests residential real estate. We only do commercial real estate.

```html
<!DOCTYPE html>
<html lang="en">
<head>
<meta charset="utf-8">
<title>Harlan Whitford – Presentation Template</title>
<link href="https://fonts.googleapis.com/css2?family=Jost:wght@500;700&family=Questrial&display=swap" rel="stylesheet">
<style>
  :root {
    --brand-red: #be1f2a;
    --tint-red: #f1d3d6;
    --paper: #ffffff;
    --stage: #000000;
  }
  html, body {
    margin: 0;
    padding: 0;
    width: 848px;
    height: 1200px;
    overflow: hidden;
    background: var(--stage);
  }
  .canvas {
    position: relative;
    width: 848px;
    height: 1200px;
    background: var(--stage);
    font-family: "Jost", "Futura", sans-serif;
  }
  .slide {
    position: absolute;
    left: 37px;
    width: 775px;
    background: var(--paper);
    overflow: hidden;
  }
  .slide--cover { top: 54px; height: 532px; }
  .slide--contents { top: 618px; height: 533px; }

  .slide__footer-band {
    position: absolute;
    left: 0;
    right: 0;
    bottom: 0;
    height: 15px;
    background: var(--brand-red);
  }

  /* Cover */
  .cover__hero {
    position: absolute;
    left: 33px;
    top: 24px;
    width: 711px;
    height: 327px;
    background: var(--brand-red);
  }
  .brand {
    position: absolute;
    right: 21px;
    top: 19px;
    text-align: right;
    color: var(--paper);
  }
  .brand__mark {
    display: block;
    width: 46px;
    height: 46px;
    margin: 0 0 30px auto;
    background: var(--paper);
  }
  .brand__name {
    display: block;
    font-weight: 700;
    font-size: 18px;
    line-height: 20px;
    letter-spacing: 0.1px;
  }
  .brand__line {
    display: block;
    font-weight: 700;
    font-size: 11.5px;
    line-height: 14px;
  }
  .cover__details {
    position: absolute;
    left: 34px;
    top: 363px;
    color: var(--brand-red);
  }
  .cover__title {
    margin: 0;
    font-weight: 700;
    font-size: 38px;
    line-height: 44px;
  }
  .cover__subtitle {
    margin: 0;
    font-weight: 700;
    font-size: 18px;
    line-height: 22px;
  }
  .cover__meta {
    margin: 8px 0 0 3px;
    font-family: "Questrial", "Century Gothic", sans-serif;
    font-size: 19px;
    line-height: 23px;
  }
  .cover__meta p { margin: 0; }

  /* Contents */
  .contents__title-bar {
    position: absolute;
    left: 24px;
    top: 15px;
    width: 728px;
    height: 58px;
    background: var(--brand-red);
  }
  .contents__title {
    margin: 0;
    padding-left: 25px;
    color: var(--paper);
    font-weight: 700;
    font-size: 30px;
    line-height: 58px;
  }
  .contents__backdrop-name {
    position: absolute;
    right: 14px;
    top: 320px;
    margin: 0;
    color: var(--tint-red);
    font-weight: 700;
    font-size: 60px;
    line-height: 62px;
    text-align: right;
  }
</style>
</head>
<body>
  <main class="canvas">
    <section class="slide slide--cover">
      <div class="cover__hero">
        <div class="brand">
          <span class="brand__mark" aria-hidden="true"></span>
          <span class="brand__name">HARLAN WHITFORD</span>
          <span class="brand__line">COMMERCIAL REAL ESTATE</span>
        </div>
      </div>
      <div class="cover__details">
        <h1 class="cover__title">Program Title</h1>
        <h2 class="cover__subtitle">Program Sub Title</h2>
        <div class="cover__meta">
          <p>Company :</p>
          <p>Date :</p>
        </div>
      </div>
      <div class="slide__footer-band"></div>
    </section>

    <section class="slide slide--contents">
      <div class="contents__title-bar">
        <h2 class="contents__title">Title Contents</h2>
      </div>
      <p class="contents__backdrop-name" aria-hidden="true">HARLAN<br>WHITFORD</p>
      <div class="slide__footer-band"></div>
    </section>
  </main>
</body>
</html>
```